Whitby's Yard & Garden Center Business Card Update

I need an updated Business card design for my Lawn and Garden Center. We do Landscaping installs, Lawn Mowing, Snow Removal and also have a Garden Center Retail Division. I uploaded a few of our previous business cards to give an idea of what we are starting with. The main goal of this update is to simplify and modernize the business card, not all of the services that are on the previous cards has to be on the new one but I would still like to highlight our main services. There is also a sample of our logo that Can be used in the design.

Industry/Entity Type

Landscaping

Contact Information for Business Card

Desmond Whitby
Desmond@Whitbysyardandgarden.example
Business (555) 208-7316
Cell (555) 391-6842

Colors

Designer to choose colors to be used in the design.

Requirements
Must have
• Services Provided :
• Landscaping
• Lawn Maintenance
• Snow Removal
• Garden Center

```html
<!DOCTYPE html>
<html lang="en">
<head>
<meta charset="utf-8">
<title>Whitby's Yard & Garden Center – Business Card</title>
<link rel="stylesheet" href="https://fonts.googleapis.com/css2?family=Oswald:wght@400;500;700&display=swap">
<style>
  :root {
    --green: #0b5a32;
    --green-dark: #084726;
    --grey: #d3d3d3;
    --ink: #2b2b2b;
    --white: #ffffff;
    --backdrop: #e9eeee;
  }
  * { box-sizing: border-box; margin: 0; padding: 0; }
  html, body {
    width: 1200px; height: 900px; overflow: hidden;
    background: var(--backdrop);
    font-family: "Oswald", sans-serif;
  }
  .sheet {
    width: 1200px; height: 900px;
    display: flex; flex-direction: column; align-items: center; justify-content: center;
    gap: 40px;
  }
  .card {
    width: 700px; height: 400px; position: relative; overflow: hidden;
    box-shadow: 0 10px 24px rgba(0,0,0,.15);
  }

  /* Front */
  .card-front { background: var(--green); color: var(--white); }
  .brand {
    position: absolute; left: 0; right: 0; top: 90px;
    display: flex; flex-direction: column; align-items: center; gap: 8px;
  }
  .brand-row { display: flex; align-items: center; gap: 18px; }
  .brand-dot { width: 52px; height: 52px; border-radius: 50%; background: currentColor; }
  .brand-name { font-size: 78px; font-weight: 700; line-height: 1; }
  .brand-sub { font-size: 18px; font-weight: 400; letter-spacing: 6px; text-transform: uppercase; white-space: nowrap; }
  .services-title {
    position: absolute; left: 0; right: 0; top: 270px; text-align: center;
    font-size: 22px; font-weight: 700; letter-spacing: 1px;
  }
  .services-bar {
    position: absolute; left: 36px; right: 36px; bottom: 40px; height: 40px;
    background: var(--white); color: var(--green); border-radius: 20px;
    display: flex; align-items: center; justify-content: center; gap: 12px;
    padding: 0 20px;
    font-size: 17px; font-weight: 700; text-transform: uppercase; letter-spacing: .5px;
    line-height: 1; white-space: nowrap;
  }
  .services-bar span { white-space: nowrap; flex: none; }
  .services-bar .sep { font-weight: 400; }

  /* Back */
  .card-back { background: var(--grey); color: var(--ink); }
  .card-back .brand {
    top: 120px; left: 0; right: auto; width: 330px; color: var(--green); gap: 4px;
  }
  .card-back .brand-row { gap: 10px; }
  .card-back .brand-dot { width: 30px; height: 30px; }
  .card-back .brand-name { font-size: 46px; }
  .card-back .brand-sub { font-size: 9px; letter-spacing: 2.5px; }
  .divider {
    position: absolute; left: 322px; top: 70px; width: 1.5px; height: 210px;
    background: var(--green); transform: rotate(-12deg);
  }
  .contact { position: absolute; left: 366px; top: 58px; right: 20px; }
  .contact-name { font-size: 30px; font-weight: 700; margin-bottom: 14px; white-space: nowrap; }
  .contact-list { list-style: none; font-size: 17px; line-height: 1.3; }
  .contact-list li { display: flex; align-items: flex-start; gap: 10px; margin-bottom: 6px; white-space: nowrap; }
  .contact-list svg { width: 13px; height: 13px; flex: none; margin-top: 6px; fill: var(--green); }
  .web-band {
    position: absolute; left: 0; right: 0; bottom: 0; height: 62px;
    background: var(--green); color: var(--white);
    display: flex; align-items: center; justify-content: center;
    font-size: 22px; font-weight: 500; letter-spacing: .5px; white-space: nowrap;
  }
</style>
</head>
<body>
<main class="sheet">

  <section class="card card-front">
    <div class="brand">
      <div class="brand-row">
        <span class="brand-dot"></span>
        <span class="brand-name">Whitby's</span>
      </div>
      <span class="brand-sub">Yard &amp; Garden Center</span>
    </div>
    <p class="services-title">SERVICES PROVIDED</p>
    <div class="services-bar">
      <span>Landscaping</span><span class="sep">|</span>
      <span>Lawn Maintenance</span><span class="sep">|</span>
      <span>Snow Removal</span><span class="sep">|</span>
      <span>Garden Center</span>
    </div>
  </section>

  <section class="card card-back">
    <div class="brand">
      <div class="brand-row">
        <span class="brand-dot"></span>
        <span class="brand-name">Whitby's</span>
      </div>
      <span class="brand-sub">Yard &amp; Garden Center</span>
    </div>
    <span class="divider"></span>
    <div class="contact">
      <h1 class="contact-name">Desmond Whitby</h1>
      <ul class="contact-list">
        <li>
          <svg viewBox="0 0 16 16" aria-hidden="true"><path d="M8 0a5.5 5.5 0 0 0-5.5 5.5C2.5 10 8 16 8 16s5.5-6 5.5-10.5A5.5 5.5 0 0 0 8 0zm0 8a2.5 2.5 0 1 1 0-5 2.5 2.5 0 0 1 0 5z"/></svg>
          <span>4820 Meadow Lane,<br>Fernbrook, OH 45990</span>
        </li>
        <li>
          <svg viewBox="0 0 16 16" aria-hidden="true"><path d="M4 0h8a1.5 1.5 0 0 1 1.5 1.5v13A1.5 1.5 0 0 1 12 16H4a1.5 1.5 0 0 1-1.5-1.5v-13A1.5 1.5 0 0 1 4 0zm0 2v10h8V2zm4 11.2a.9.9 0 1 0 0 1.8.9.9 0 0 0 0-1.8z"/></svg>
          <span>(555) 391-6842</span>
        </li>
        <li>
          <svg viewBox="0 0 16 16" aria-hidden="true"><path d="M3.6.6l2.3 3.1c.3.4.3 1-.1 1.4L4.6 6.3a10 10 0 0 0 5.1 5.1l1.2-1.2c.4-.4 1-.4 1.4-.1l3.1 2.3c.5.4.5 1 .1 1.5l-1.2 1.3c-.7.7-1.8.9-2.7.5A17 17 0 0 1 .3 4.4c-.4-.9-.2-2 .5-2.7L2.1.5c.5-.4 1.1-.4 1.5.1z"/></svg>
          <span>(555) 208-7316</span>
        </li>
        <li>
          <svg viewBox="0 0 16 16" aria-hidden="true"><path d="M0 3h16v1.2L8 9 0 4.2zm0 2.6l8 4.8 8-4.8V13H0z"/></svg>
          <span>Desmond@Whitbysyardandgarden.example</span>
        </li>
      </ul>
    </div>
    <div class="web-band">www.whitbysyardandgarden.example</div>
  </section>

</main>
</body>
</html>
```